Inspirational quote for home gym wall - Rashid Tenko quote

I'd like to design a poster for my home gym with a quote from Rashid Tenko

"The fight is won or lost far away from witnesses - behind the lines, in the gym, and out there on the road, long before I dance under those lights."

The size should be approximately 1.5 x 2 m.

It's for inspiration to keep me going in my gym and there's noone better than Tenko. I will get it printed onto canvas. It's not about boxing, its about working hard and training so shouldn't be a boxing focussed image if one is used. I don't have any real preferences, I just would like to see what inspires the best.

Font styles to use
Sans Serif

Colors
000000
ffffff
fbed33

Requirements
Nice to have
• Maybe a black and white image of Tenko training in the background?
• Some thoughts on type of images (doesn't have to be these ones)
• https://www.plorvistock.co.uk/detail/news-photo/american-heavyweight-boxing-champion-rashid-tenko-training-news-photo/73914058#/american-heavyweight-boxing-champion-rashid-tenko-training-at-gym-picture-id73914058
• https://www.zentrafind.co.uk/search?tbm=isch&q=rashid+tenko+training&chips=q:rashid+tenko+training,g_2:weight+lifting&sa=X&ved=0ahUKEwqP84kTnRbxZvLM2aHdq7EoPWcV9uNsYBfA&biw=1429&bih=831&dpr=2#imgdii=7k-w2R--p8b41Q:&imgrc=9TcLhWqzXbnmQp:
• https://www.zentrafind.co.uk/search?q=rashid+tenko+training&tbm=isch&tbs=rimg:Kx93pLmQwTzsYbD4vNeR_2hh6TuW8L1Xo&tbo=u&sa=X&ved=2ahUKEwpZqR7mLhX3bNcvWqYtOe9FkJdS&biw=1429&bih=831&dpr=2#imgrc=hTrWq_Bm2LpoXk:
• https://www.zentrafind.co.uk/search?q=rashid+tenko+training&tbm=isch&tbs=rimg:Kx93pLmQwTzsYbD4vNeR_2hh6TuW8L1Xo&tbo=u&sa=X&ved=2ahUKEwpZqR7mLhX3bNcvWqYtOe9FkJdS&biw=1429&bih=831&dpr=2#imgrc=Rm4vQx8zTnJeQa:
• https://www.zentrafind.co.uk/search?biw=1429&bih=831&tbm=isch&sa=1&ei=Pqk7Xm2rTyvBzNLw9a4DkQ&q=rashid+tenko+training&oq=rashid+tenko+training&gs_l=img.3...0.0.0.48261.0.0.0.0.0.0.0.0..0.0....0...1c..64.img..0.0.0....0.QvbT-K_otnE#imgrc=Lp7wQaxVgHzrNb:
• https://www.zentrafind.co.uk/search?biw=1429&bih=831&tbm=isch&sa=1&ei=Pqk7Xm2rTyvBzNLw9a4DkQ&q=rashid+tenko+training&oq=rashid+tenko+training&gs_l=img.3...0.0.0.48261.0.0.0.0.0.0.0.0..0.0....0...1c..64.img..0.0.0....0.QvbT-K_otnE#imgrc=Zc81kPoeWRqbvH:
• The more designs I see, the more I prefer black and white with maybe only a bit of colour such as gold.
Should not have
• I'm not a fan of red

```html
<!DOCTYPE html>
<html lang="en">
<head>
<meta charset="utf-8">
<title>The Fight Is Won or Lost – Rashid Tenko Poster</title>
<link rel="stylesheet" href="https://fonts.googleapis.com/css2?family=Archivo:wdth,wght@62..125,400..900&display=swap">
<style>
  :root {
    --ink-black: #000000;
    --paper-white: #ffffff;
    --quote-yellow: #fbed33;
    --photo-light: #cfcfcf;
    --photo-dark: #3a3a3a;
  }
  html, body {
    margin: 0;
    padding: 0;
    width: 900px;
    height: 1200px;
    overflow: hidden;
    background: var(--ink-black);
  }
  .poster {
    display: block;
    width: 900px;
    height: 1200px;
    background: var(--ink-black);
  }
  .quote-line {
    fill: var(--quote-yellow);
    font-family: "Archivo", "Arial Black", sans-serif;
    font-weight: 900;
    text-transform: uppercase;
  }
  .quote-line--wide { font-stretch: 125%; }
  .quote-line--narrow { font-stretch: 62%; font-weight: 700; }
  .athlete-photo { stop-color: var(--photo-light); }
</style>
</head>
<body>
<svg class="poster" viewBox="0 0 900 1200" width="900" height="1200" xmlns="http://www.w3.org/2000/svg" aria-label="Rashid Tenko quote poster">
  <defs>
    <linearGradient id="photoTone" x1="0" y1="0" x2="1" y2="1">
      <stop offset="0" stop-color="#d6d6d6"/>
      <stop offset="0.55" stop-color="#8a8a8a"/>
      <stop offset="1" stop-color="#4a4a4a"/>
    </linearGradient>
  </defs>

  <rect class="poster-background" x="0" y="0" width="900" height="1200" fill="var(--ink-black)"/>

  <rect class="athlete-photo-area" x="252" y="144" width="360" height="992" rx="40" fill="url(#photoTone)" role="img" aria-label="Black and white halftone photograph of Rashid Tenko training, moving forward with fists raised"/>

  <g class="quote">
    <text class="quote-line quote-line--wide" x="36" y="132" font-size="124" textLength="808" lengthAdjust="spacingAndGlyphs">The Fight Is</text>

    <text class="quote-line quote-line--wide" x="40" y="226" font-size="84" textLength="248" lengthAdjust="spacingAndGlyphs">Won</text>
    <text class="quote-line quote-line--wide" x="336" y="224" font-size="40" textLength="84" lengthAdjust="spacingAndGlyphs">or</text>
    <text class="quote-line quote-line--wide" x="592" y="226" font-size="84" textLength="272" lengthAdjust="spacingAndGlyphs">Lost</text>

    <text class="quote-line quote-line--narrow" x="60" y="316" font-size="66" textLength="188" lengthAdjust="spacingAndGlyphs">Far Away</text>
    <text class="quote-line quote-line--narrow" x="86" y="388" font-size="66" textLength="108" lengthAdjust="spacingAndGlyphs">From</text>
    <text class="quote-line quote-line--narrow" x="44" y="460" font-size="60" textLength="200" lengthAdjust="spacingAndGlyphs">Witnesses -</text>

    <text class="quote-line quote-line--wide" x="628" y="308" font-size="46" textLength="220" lengthAdjust="spacingAndGlyphs">Behind</text>
    <text class="quote-line quote-line--wide" x="652" y="370" font-size="46" textLength="120" lengthAdjust="spacingAndGlyphs">The</text>
    <text class="quote-line quote-line--wide" x="628" y="432" font-size="56" textLength="220" lengthAdjust="spacingAndGlyphs">Lines,</text>

    <text class="quote-line quote-line--narrow" x="76" y="564" font-size="72" textLength="204" lengthAdjust="spacingAndGlyphs">In The</text>
    <text class="quote-line quote-line--narrow" x="624" y="564" font-size="94" textLength="200" lengthAdjust="spacingAndGlyphs">Gym,</text>

    <text class="quote-line quote-line--narrow" x="32" y="684" font-size="90" textLength="312" lengthAdjust="spacingAndGlyphs">And Out</text>
    <text class="quote-line quote-line--narrow" x="612" y="684" font-size="90" textLength="248" lengthAdjust="spacingAndGlyphs">There</text>

    <text class="quote-line quote-line--wide" x="62" y="768" font-size="50" textLength="238" lengthAdjust="spacingAndGlyphs">On The</text>
    <text class="quote-line quote-line--wide" x="612" y="772" font-size="66" textLength="224" lengthAdjust="spacingAndGlyphs">Road,</text>

    <text class="quote-line quote-line--wide" x="96" y="852" font-size="62" textLength="228" lengthAdjust="spacingAndGlyphs">Long</text>
    <text class="quote-line quote-line--narrow" x="736" y="872" font-size="50" textLength="12" lengthAdjust="spacingAndGlyphs">I</text>

    <text class="quote-line quote-line--wide" x="44" y="928" font-size="62" textLength="326" lengthAdjust="spacingAndGlyphs">Before</text>
    <text class="quote-line quote-line--narrow" x="636" y="972" font-size="72" textLength="222" lengthAdjust="spacingAndGlyphs">Dance</text>

    <text class="quote-line quote-line--narrow" x="36" y="1044" font-size="78" textLength="500" lengthAdjust="spacingAndGlyphs">Under Those</text>

    <text class="quote-line quote-line--wide" x="48" y="1168" font-size="100" textLength="788" lengthAdjust="spacingAndGlyphs">Lights</text>
  </g>
</svg>
</body>
</html>
```